Canyon Ridge Early Jump Ball Hoops Classic

This is a flyer to advertise a boys & girls basketball tournament. It will be emailed out to various clubs/organizations in the West in attempt to get them to register for the tournament.
I would like it to have black background with a watermark background of the Salt Lake City city scape. The city scape needs to include the Mountains and downtown buildings of SLC. I would also like a pic of a couple basketball players on the flyer

Colors
85cae6
ffffff

Requirements
Must have
• Black background
• Salt Lake City city scape watermark (showing mountains and downtown buildings)
• Use uploaded info
• Use 1 or 2 uploaded basketball player pics
Nice to have
• Use Carolina blue, black, silver & white for colors

```html
<!DOCTYPE html>
<html lang="en">
<head>
<meta charset="utf-8">
<title>Canyon Ridge Early Jump Ball Hoops Classic – Flyer</title>
<link href="https://fonts.googleapis.com/css2?family=Stardos+Stencil:wght@700&family=PT+Sans:wght@400;700&display=swap" rel="stylesheet">
<style>
  :root{
    --carolina:#85cae6;
    --white:#ffffff;
    --black:#050505;
    --silver:#bfc4c8;
    --wood-light:#c48a55;
    --wood-dark:#6e4020;
    --page:#e4e4e4;
    --ink:#0b0b0b;
  }
  *{box-sizing:border-box;margin:0;padding:0}
  html,body{width:1105px;height:1200px;overflow:hidden;background:var(--page)}
  .flyer{position:absolute;left:122px;top:44px;width:860px;height:1113px;background:var(--black);overflow:hidden;font-family:"PT Sans",sans-serif;color:var(--white)}
  .flyer > *{z-index:3}
  .skyline{position:absolute;left:0;top:190px;width:860px;height:360px;z-index:0;background:linear-gradient(180deg,rgba(60,60,60,0) 0%,rgba(70,70,70,.7) 45%,rgba(40,40,40,.55) 80%,rgba(5,5,5,0) 100%)}
  .corner-stripes{position:absolute;inset:0;z-index:1}
  .floor{position:absolute;left:0;top:820px;width:860px;height:293px;z-index:0;background:linear-gradient(180deg,rgba(110,64,32,0) 0%,var(--wood-dark) 16%,var(--wood-light) 55%,#a86e3e 100%)}
  .player{position:absolute;left:575px;top:95px;width:250px;height:870px;z-index:1;border-radius:125px 125px 40px 40px;background:linear-gradient(180deg,#9a8b7f 0%,var(--carolina) 22%,#7fb8d8 60%,#2c3f7a 100%)}
  .ball{position:absolute;left:430px;top:335px;width:110px;height:110px;z-index:2;border-radius:50%;background:radial-gradient(circle at 40% 35%,#e07a35,#b2511c 70%,#7c3310)}
  .tournament-mark{position:absolute;left:250px;top:92px;width:250px;height:200px;background:var(--white);border-radius:16px;display:flex;align-items:center;justify-content:center;text-align:center;padding:18px}
  .tournament-name{font-weight:700;font-size:25px;line-height:1.15;color:var(--ink);text-transform:uppercase}
  .headline{position:absolute;left:30px;top:510px;font-family:"Stardos Stencil",serif;font-weight:700;line-height:1}
  .headline .line-1{font-size:46px;color:var(--white)}
  .headline .line-2{font-size:46px;color:var(--carolina);margin-top:4px}
  .feature-band{position:absolute;left:0;top:625px;width:620px;height:105px}
  .feature-band svg{position:absolute;inset:0}
  .feature-text{position:absolute;left:34px;top:10px;color:var(--ink)}
  .feature-text .big{font-weight:700;font-size:24px;line-height:1.15;text-transform:uppercase}
  .feature-text .small{font-weight:700;font-size:16px;margin-top:3px}
  .details{position:absolute;left:34px;top:752px;font-family:"Stardos Stencil",serif;font-weight:700;font-size:26px;line-height:1.35;text-transform:uppercase}
  .details .label{color:var(--carolina)}
  .cost-sticker{position:absolute;left:520px;top:760px;width:112px;height:112px;border-radius:50%;background:radial-gradient(circle at 40% 30%,var(--white),#cfe9f5 70%,#a9d4e8);display:flex;flex-direction:column;align-items:center;justify-content:center;font-family:"Stardos Stencil",serif;font-weight:700;color:var(--ink);font-size:19px;line-height:1.1;box-shadow:0 4px 10px rgba(0,0,0,.5)}
  .venue{position:absolute;left:34px;top:880px}
  .venue .tag{font-weight:700;font-size:30px;color:var(--carolina);text-transform:uppercase;line-height:1.2}
  .venue .address{font-weight:700;font-size:20px;line-height:1.2;margin-top:2px}
  .contact-band{position:absolute;left:0;top:1002px;width:860px;height:38px;background:var(--carolina);color:var(--ink);display:flex;align-items:center;gap:60px;padding-left:34px;font-weight:700;font-size:21px}
  .contact-band span{display:flex;align-items:center;gap:10px}
  .fine-print{position:absolute;left:34px;top:1048px;width:800px;font-size:9px;line-height:1.2;color:var(--white)}
</style>
</head>
<body>
<main class="flyer">
  <div class="skyline" role="img" aria-label="Faint watermark of the Salt Lake City skyline with mountains and downtown buildings"></div>
  <svg class="corner-stripes" width="860" height="1113" viewBox="0 0 860 1113" aria-hidden="true">
    <polygon points="0,170 0,200 250,110 250,92" fill="var(--carolina)"/>
    <polygon points="720,0 860,0 860,70" fill="var(--carolina)"/>
  </svg>
  <div class="floor" role="img" aria-label="Wooden basketball court floor"></div>
  <div class="player" role="img" aria-label="Photo of a youth basketball player in a light blue uniform dribbling"></div>
  <div class="ball" role="img" aria-label="Basketball"></div>

  <div class="tournament-mark">
    <p class="tournament-name">Canyon Ridge Early Jump Ball Hoops Classic</p>
  </div>

  <h1 class="headline">
    <div class="line-1">YBA SUPER REGIONAL</div>
    <div class="line-2">NATIONAL QUALIFIER</div>
  </h1>

  <section class="feature-band">
    <svg width="620" height="105" viewBox="0 0 620 105" aria-hidden="true">
      <polygon points="0,0 620,0 585,105 0,105" fill="var(--carolina)"/>
    </svg>
    <div class="feature-text">
      <p class="big">4 Game Guarantee</p>
      <p class="big">West Coast Super Regional Event.</p>
      <p class="small">Already confirmed teams from UT, NV, OR, ID, CO, WY, CA, WA, MT</p>
    </div>
  </section>

  <section class="details">
    <p><span class="label">Date:</span> May 5-6</p>
    <p><span class="label">Grades:</span> Boys &amp; Girls 2nd – 8th</p>
    <p><span class="label">Divisions:</span> Div I &amp; Div II</p>
  </section>

  <div class="cost-sticker"><span>COST</span><span>$425/TEAM</span></div>

  <section class="venue">
    <p class="tag">All Under 1 Roof</p>
    <p class="address">Summit Court Events Center<br>2150 W. 900 S.<br>Salt Lake City, UT</p>
  </section>

  <section class="contact-band">
    <span>
      <svg width="24" height="17" viewBox="0 0 24 17" aria-hidden="true"><rect x="1" y="1" width="22" height="15" fill="var(--ink)"/><polyline points="1,1 12,10 23,1" fill="none" stroke="var(--carolina)" stroke-width="2"/></svg>
      coach@canyonridgehoops.com
    </span>
    <span>
      <svg width="18" height="18" viewBox="0 0 24 24" aria-hidden="true"><path d="M6.6 10.8a15 15 0 0 0 6.6 6.6l2.2-2.2c.3-.3.7-.4 1-.2 1.1.4 2.3.6 3.6.6.6 0 1 .4 1 1V20c0 .6-.4 1-1 1A17 17 0 0 1 3 4c0-.6.4-1 1-1h3.5c.6 0 1 .4 1 1 0 1.3.2 2.5.6 3.6.1.3 0 .7-.2 1z" fill="var(--ink)"/></svg>
      (801) 555-0142
    </span>
  </section>

  <section class="fine-print">
    <p>• This event is licensed by the Youth Basketball Alliance of America.</p>
    <p>• All participants must have a current YBA membership.</p>
    <p>• YBA membership may not be included as part of the entry fee to the event.</p>
    <p>• YBA membership must be obtained before the competition begins except where the event operator has a laptop available with an internet connection.</p>
    <p>• Participants are encouraged to visit the YBA web site www.ybahoops.org to obtain their membership.</p>
  </section>
</main>
</body>
</html>
```